Business Card for a Floral & Decorating Business

I would like to take my current logo and create a better business card. I am looking for elegance as I am a florist and event decorator. My logo has multiple colour options. I like colours like green, purple, pink and orange, I think I would like a white card, open to black back ground. I want it to feel elegant and romantic. I like metallic lettering that maybe is indented in the paper, I also like glossy paper. I have a full logo already as well as a badge. I have attached both in multiple colours.m

Target Market(s)

Weddings, special events, floral customers

Industry/Entity Type

Floral and decorating

Contact Information for Business Card

Phone number, email, instagram, facebook, title, name, logo

Font styles to use
Script

Requirements
Nice to have
• Elegant

```html
<!DOCTYPE html>
<html lang="en">
<head>
<meta charset="utf-8">
<title>Marlowe Ashby – Business Card</title>
<link href="https://fonts.googleapis.com/css2?family=Pinyon+Script&family=Raleway:wght@400;500&display=swap" rel="stylesheet">
<style>
  :root {
    --backdrop: #e4e5e4;
    --card: #7d6491;
    --card-light: #8a73a0;
    --ink-light: #f1ecf4;
    --ink-soft: #ddd3e4;
    --ink-dark: #2b2030;
    --floral-tint: rgba(255, 255, 255, 0.07);
  }
  * { margin: 0; padding: 0; box-sizing: border-box; }
  html, body { width: 1200px; height: 1200px; overflow: hidden; }
  body { background: var(--backdrop); position: relative; font-family: "Raleway", sans-serif; }

  .card {
    position: absolute;
    left: 282px;
    width: 636px;
    height: 366px;
    border-radius: 20px;
    background: var(--card);
    overflow: hidden;
    box-shadow: 0 4px 10px rgba(0, 0, 0, 0.18);
  }
  .card--front { top: 194px; }
  .card--back { top: 640px; }

  /* Front */
  .monogram {
    position: absolute;
    display: flex;
    align-items: center;
    gap: 8px;
    color: var(--ink-light);
    font-family: "Raleway", sans-serif;
    font-weight: 500;
  }
  .monogram__dot {
    width: 10px; height: 10px;
    border-radius: 50%;
    background: var(--ink-light);
  }
  .card--front .monogram { left: 54px; top: 96px; font-size: 17px; letter-spacing: 0.5px; }

  .floral-accent {
    position: absolute;
    left: 438px; top: 18px;
    width: 170px; height: 348px;
    border-radius: 80px 0 0 0;
    background: radial-gradient(ellipse at 60% 55%, var(--floral-tint), transparent 70%);
  }

  .identity {
    position: absolute;
    right: 62px;
    top: 172px;
    text-align: right;
  }
  .identity__name {
    font-family: "Pinyon Script", cursive;
    font-size: 40px;
    color: var(--ink-light);
    line-height: 1.1;
    font-weight: 400;
  }
  .identity__title {
    font-size: 16px;
    color: var(--ink-soft);
    letter-spacing: 0.3px;
    margin-top: 2px;
  }
  .divider {
    position: absolute;
    left: 55px; top: 263px;
    width: 521px; height: 1px;
    background: var(--ink-soft);
    opacity: 0.8;
  }
  .contact {
    position: absolute;
    right: 58px;
    top: 278px;
    list-style: none;
    text-align: right;
    color: var(--ink-soft);
    font-size: 14px;
    line-height: 21px;
    letter-spacing: 0.3px;
  }
  .contact li { display: flex; align-items: center; justify-content: flex-end; gap: 8px; }
  .contact svg { width: 12px; height: 12px; fill: var(--ink-light); }

  /* Back */
  .card--back .monogram {
    left: 0; right: 0; top: 82px;
    justify-content: center;
    flex-direction: column;
    gap: 14px;
  }
  .brand-mark {
    width: 14px; height: 14px;
    border-radius: 50%;
    background: var(--ink-dark);
  }
  .brand-name {
    font-family: "Pinyon Script", cursive;
    font-size: 58px;
    color: var(--ink-dark);
    line-height: 1;
  }
  .social {
    position: absolute;
    left: 0; right: 0; top: 310px;
    display: flex;
    justify-content: center;
    gap: 20px;
  }
  .social__dot {
    width: 18px; height: 18px;
    border-radius: 50%;
    background: var(--ink-light);
  }
</style>
</head>
<body>

<section class="card card--front" aria-label="Card front">
  <div class="floral-accent" role="img" aria-label="Faint line-drawn floral decoration"></div>
  <div class="monogram"><span class="monogram__dot"></span>Marlowe Ashby</div>
  <div class="identity">
    <h1 class="identity__name">Marlowe Ashby</h1>
    <p class="identity__title">Floral Stylist</p>
  </div>
  <div class="divider"></div>
  <ul class="contact">
    <li>555.014.2290
      <svg viewBox="0 0 24 24" aria-hidden="true"><path d="M6.6 10.8a15.1 15.1 0 0 0 6.6 6.6l2.2-2.2a1 1 0 0 1 1-.25 11.4 11.4 0 0 0 3.6.57 1 1 0 0 1 1 1V20a1 1 0 0 1-1 1A17 17 0 0 1 3 4a1 1 0 0 1 1-1h3.5a1 1 0 0 1 1 1c0 1.25.2 2.45.57 3.57a1 1 0 0 1-.25 1z"/></svg>
    </li>
    <li>info@marloweashby.com
      <svg viewBox="0 0 24 24" aria-hidden="true"><path d="M2 5h20v14H2z M2 5l10 8 10-8" fill="var(--ink-light)" stroke="var(--card)" stroke-width="1.5"/></svg>
    </li>
  </ul>
</section>

<section class="card card--back" aria-label="Card back">
  <div class="monogram">
    <span class="brand-mark"></span>
    <span class="brand-name">Marlowe Ashby</span>
  </div>
  <div class="social" aria-label="Social profiles">
    <span class="social__dot"></span>
    <span class="social__dot"></span>
  </div>
</section>

</body>
</html>
```